Fernly Garage Doors Business Card

I need a Business Card for my garage door business:
Fernly Garage Doors.
please add:
logo
phone number: 833-2-FERNLY
(337-659)

email: service@fernlygaragedoors.com
website: www.fernlygaragedoors.com

The attached image is recommendation ONLY.

```html
<!DOCTYPE html>
<html lang="en">
<head>
<meta charset="utf-8">
<title>Fernly Garage Doors Business Card</title>
<link href="https://fonts.googleapis.com/css2?family=Source+Sans+3:wght@400;600&display=swap" rel="stylesheet">
<style>
  :root {
    --backdrop: #3a302b;
    --card: #151515;
    --card-edge: #0c0c0c;
    --teal: #4cc3c9;
    --white: #f2f2f2;
    --muted: #9a9a9a;
  }
  * { box-sizing: border-box; margin: 0; padding: 0; }
  html, body { width: 1200px; height: 814px; overflow: hidden; }
  body {
    background: var(--backdrop);
    font-family: "Source Sans 3", sans-serif;
    display: flex;
    align-items: center;
    justify-content: center;
    gap: 40px;
  }
  .card {
    position: relative;
    width: 540px;
    height: 309px;
    background: var(--card);
    border: 1px solid var(--card-edge);
    color: var(--white);
  }
  .brand {
    position: absolute;
    display: flex;
    align-items: center;
    gap: 16px;
  }
  .brand-mark {
    width: 62px; height: 62px;
    border-radius: 50%;
    background: var(--teal);
    flex: none;
  }
  .brand-name {
    font-weight: 600;
    font-size: 25px;
    line-height: 1.05;
    color: var(--white);
    width: 180px;
  }
  .front .brand { left: 62px; top: 70px; }
  .divider {
    position: absolute;
    left: 262px; top: 158px;
    width: 1px; height: 92px;
    background: var(--muted);
  }
  .person {
    position: absolute;
    right: 292px; top: 196px;
    text-align: right;
  }
  .person-name { color: var(--teal); font-size: 19px; font-weight: 600; }
  .person-title { color: var(--white); font-size: 14px; }
  .contacts {
    position: absolute;
    left: 280px; top: 162px;
    list-style: none;
    font-size: 13.5px;
    line-height: 1.45;
  }
  .contacts li { display: flex; align-items: center; gap: 8px; }
  .contacts svg { width: 12px; height: 12px; fill: var(--teal); flex: none; }
  .contacts .spacer { width: 12px; flex: none; }
  .back .brand { left: 130px; top: 100px; }
  .back .brand-mark { background: var(--white); width: 72px; height: 72px; }
  .back .brand-name { font-size: 28px; width: 220px; }
  .website {
    position: absolute;
    left: 0; right: 0; top: 208px;
    text-align: center;
    font-size: 12px;
    letter-spacing: 2.4px;
    color: var(--white);
  }
</style>
</head>
<body>
  <section class="card front">
    <div class="brand">
      <span class="brand-mark"></span>
      <span class="brand-name">Fernly Garage Doors</span>
    </div>
    <div class="person">
      <p class="person-name">Dale Morgan</p>
      <p class="person-title">CEO/Founder</p>
    </div>
    <span class="divider"></span>
    <ul class="contacts">
      <li><svg viewBox="0 0 12 12"><path d="M2.5 0.5l2 2-1.2 1.5c.8 1.8 2 3 3.7 3.7L8.5 6.5l2 2L9 11C4.5 10.6 1.4 7.5 1 3z"/></svg>833-2-FERNLY</li>
      <li><svg viewBox="0 0 12 12"><path d="M2.5 0.5l2 2-1.2 1.5c.8 1.8 2 3 3.7 3.7L8.5 6.5l2 2L9 11C4.5 10.6 1.4 7.5 1 3z"/></svg>(337-659)</li>
      <li><svg viewBox="0 0 12 12"><path d="M0 2.5h12v7H0z M0 2.5l6 4 6-4" /><path d="M0.8 3l5.2 3.5L11.2 3" stroke="#151515" stroke-width="1" fill="none"/></svg>service@fernlygaragedoors.com</li>
      <li><svg viewBox="0 0 12 12"><circle cx="6" cy="6" r="5.5"/><path d="M0.5 6h11M6 0.5c-2.5 3-2.5 8 0 11M6 0.5c2.5 3 2.5 8 0 11" stroke="#151515" stroke-width="0.9" fill="none"/></svg>www.fernlygaragedoors.com</li>
    </ul>
  </section>

  <section class="card back">
    <div class="brand">
      <span class="brand-mark"></span>
      <span class="brand-name">Fernly Garage Doors</span>
    </div>
    <p class="website">www.fernlygaragedoors.com</p>
  </section>
</body>
</html>
```